Billboard for RV Park

I am looking for a new billboard design for our RV park. The dimensions are 10' tall x 40' long. It will be illuminated at night and printed on vinyl.
To give you an idea of our park, you can look at our website at http://www.hollowpinecamp.com/
The things I want on the sign are:
-Exit Now (In large letters)
-Mention of the cedarlark cafe
-"Wifi and Cable"
-"Large Pull though sites"
-Kind Rolf logo (I have two options attached)
I have also attached what our other billboard looks like. The new one does not need to look anything like it, but I thought I'd show an example. The new billboard is bigger, so it has room for more info on it.
I don't have any specific ideas on the design, but I would like it to be eye catching.

```html
<!DOCTYPE html>
<html lang="en">
<head>
<meta charset="utf-8">
<title>Hollow Pine RV Park and Cedarlark Cafe Billboard</title>
<link rel="stylesheet" href="https://fonts.googleapis.com/css2?family=Anton&family=Archivo+Black&display=swap">
<style>
  :root {
    --page-bg: #d6d8db;
    --sky-top: #123f8c;
    --sky-bottom: #3f86d4;
    --band-blue: #0c4a94;
    --band-edge: #2c6fc0;
    --brand-maroon: #7a1e2a;
    --ink-black: #0b0b0b;
    --paper-white: #ffffff;
    --hex-navy: #1d2f55;
    --hex-green: #6aa23a;
    --hex-yellow: #e2c81c;
    --hex-blue: #1e8fe0;
    --hex-purple: #8a3c8f;
  }
  html, body {
    margin: 0;
    width: 1200px;
    height: 498px;
    overflow: hidden;
    background: var(--page-bg);
  }
  .billboard {
    position: absolute;
    left: 33px;
    top: 106px;
    width: 1134px;
    height: 286px;
    overflow: hidden;
    background: linear-gradient(180deg, var(--sky-top) 0%, var(--sky-bottom) 100%);
    box-shadow: 0 0 0 4px var(--paper-white);
  }
  .park-photo {
    position: absolute;
    left: 0;
    top: 100px;
    width: 1010px;
    height: 132px;
    background: linear-gradient(180deg, #7fb8e6 0%, #b9d7ea 28%, #5e8c3a 46%, #7c9c52 66%, #b8b4a6 82%, #9c9888 100%);
  }
  .brand-mark {
    position: absolute;
    left: 62px;
    top: 30px;
    width: 78px;
    height: 78px;
    border-radius: 50%;
    background: var(--hex-navy);
  }
  .brand-name {
    position: absolute;
    left: 192px;
    top: 34px;
    margin: 0;
    font-family: "Anton", sans-serif;
    font-size: 24px;
    line-height: 1;
    letter-spacing: 2px;
    color: var(--paper-white);
    text-transform: uppercase;
  }
  .headline {
    position: absolute;
    left: 160px;
    top: 62px;
    margin: 0;
    font-family: "Anton", sans-serif;
    font-weight: 400;
    color: var(--brand-maroon);
    line-height: 1;
    text-transform: uppercase;
    -webkit-text-stroke: 0;
    text-shadow: 2px 0 0 var(--paper-white), -2px 0 0 var(--paper-white), 0 2px 0 var(--paper-white), 0 -2px 0 var(--paper-white), 2px 2px 0 var(--paper-white), -2px -2px 0 var(--paper-white), 2px -2px 0 var(--paper-white), -2px 2px 0 var(--paper-white), 3px 4px 4px rgba(0,0,0,0.5);
  }
  .headline-line { display: block; white-space: nowrap; }
  .headline-park { margin-left: 6px; }
  .headline-rv { font-size: 58px; }
  .headline-mid { font-size: 50px; }
  .headline-and { font-size: 34px; }
  .headline-cafe-line { margin-top: -2px; }
  .headline-cafe-name { font-size: 60px; letter-spacing: 1px; }
  .headline-cafe { font-size: 40px; margin-left: 10px; }
  .exit-now {
    position: absolute;
    left: 630px;
    top: 16px;
    margin: 0;
    font-family: "Anton", sans-serif;
    font-size: 64px;
    line-height: 1;
    letter-spacing: 3px;
    color: var(--ink-black);
    text-shadow: 2px 0 0 var(--paper-white), -2px 0 0 var(--paper-white), 0 2px 0 var(--paper-white), 0 -2px 0 var(--paper-white), 2px 2px 0 var(--paper-white), -2px -2px 0 var(--paper-white), 2px -2px 0 var(--paper-white), -2px 2px 0 var(--paper-white);
  }
  .amenity-band {
    position: absolute;
    left: 0;
    bottom: 0;
    width: 100%;
    height: 54px;
    background: var(--band-blue);
    border-top: 3px solid var(--band-edge);
  }
  .amenities {
    position: absolute;
    left: 136px;
    top: 10px;
    margin: 0;
    font-family: "Archivo Black", sans-serif;
    font-size: 26px;
    line-height: 1.2;
    color: var(--paper-white);
    text-shadow: 2px 2px 0 var(--ink-black), -1px -1px 0 var(--ink-black), 1px -1px 0 var(--ink-black), -1px 1px 0 var(--ink-black);
    white-space: nowrap;
  }
  .hex-gallery {
    position: absolute;
    left: 0;
    top: 0;
    width: 1134px;
    height: 286px;
    z-index: 2;
  }
</style>
</head>
<body>
  <main class="billboard">
    <div class="park-photo" role="img" aria-label="Panoramic photo of the RV park with trees, green shrubs and parked RVs under a blue sky"></div>

    <div class="brand-mark" aria-hidden="true"></div>
    <p class="brand-name">Hollow Pine</p>

    <h1 class="headline">
      <span class="headline-line headline-park"><span class="headline-rv">RV</span> <span class="headline-mid">Park</span> <span class="headline-and">and</span></span>
      <span class="headline-line headline-cafe-line"><span class="headline-cafe-name">Cedarlark</span><span class="headline-cafe">Cafe</span></span>
    </h1>

    <p class="exit-now">EXIT NOW</p>

    <div class="amenity-band">
      <p class="amenities">LARGE PULL . FREE WIFI AND CABLE</p>
    </div>

    <svg class="hex-gallery" viewBox="0 0 1134 286">
      <g class="hex-accents" aria-hidden="true">
        <polygon points="993,28 1012,39 1012,61 993,72 974,61 974,39" fill="var(--hex-navy)" opacity="0.9"/>
        <polygon points="1012,72 1020,77 1020,86 1012,91 1004,86 1004,77" fill="var(--paper-white)"/>
        <polygon points="1089,106 1105,115 1105,133 1089,142 1073,133 1073,115" fill="var(--hex-green)" opacity="0.85"/>
        <polygon points="902,140 921,151 921,173 902,184 883,173 883,151" fill="var(--hex-yellow)" opacity="0.75"/>
        <polygon points="944,200 953,205 953,215 944,220 935,215 935,205" fill="var(--hex-yellow)"/>
        <polygon points="924,222 941,232 941,252 924,262 907,252 907,232" fill="var(--hex-navy)" opacity="0.8"/>
        <polygon points="1107,148 1114,152 1114,160 1107,164 1100,160 1100,152" fill="var(--hex-blue)"/>
        <polygon points="1134,164 1148,172 1148,188 1134,196 1120,188 1120,172" fill="var(--hex-purple)"/>
        <polygon points="1014,200 1022,204 1022,214 1014,218 1006,214 1006,204" fill="var(--hex-blue)" opacity="0.8"/>
      </g>
      <polygon role="img" aria-label="Photo of the cafe dining room with tables and windows" points="1071,8 1120,36 1120,94 1071,122 1022,94 1022,36" fill="#c48a4e" stroke="var(--paper-white)" stroke-width="3"/>
      <polygon role="img" aria-label="Photo of the RV sites with trees and gravel pads" points="1021,93 1070,121 1070,179 1021,207 972,179 972,121" fill="#9fb77e" stroke="var(--paper-white)" stroke-width="3"/>
      <polygon role="img" aria-label="Photo of the swimming pool with a thatched umbrella" points="1071,174 1120,201 1120,256 1071,283 1022,256 1022,201" fill="#2bb3e0" stroke="var(--paper-white)" stroke-width="3"/>
    </svg>
  </main>
</body>
</html>
```